Morden, Creative, Unique, Independent Wine Shop

1. We are a brand new wine shop located in Melbourne Australia, we have our logo already, simply use the logo to design a business card.
2. I have uploaded our logo in two versions, with or without shadow, any of them is acceptable.
3. Make it as creative and unique as possible, no limitation of shape, color combination, geometry pattern, fonts, composing etc.
3. Info on the card:
- Brambleford Wine Cellar (Not very necessary if logo is obviously shown)
- 42 Carrow Steet, Wexbury, Victoria, Australia 3207
- +61 3 9418 7360
- www.bramblefordwinecellar.example.au
- bramblefordwinecellar@mailbox.example
- Additional icons: Google, Instagram, Facebook, Twitter
4. Once again, forget it is a commercial card, make it special.

```html
<!DOCTYPE html>
<html lang="en">
<head>
<meta charset="utf-8">
<title>Brambleford Wine Cellar – Business Card</title>
<link rel="stylesheet" href="https://fonts.googleapis.com/css2?family=Tinos&family=Roboto:wght@700&display=swap">
<style>
  :root {
    --wine: #9e0e30;
    --ink: #000000;
    --paper: #ffffff;
    --backdrop: #ffffff;
  }
  html, body {
    margin: 0;
    width: 1200px;
    height: 319px;
    overflow: hidden;
    background: var(--backdrop);
  }
  .sheet { position: relative; width: 1200px; height: 319px; }
  .card {
    position: absolute;
    top: 0;
    width: 564px;
    height: 319px;
    box-sizing: border-box;
    border: 2px solid var(--ink);
    background: var(--paper);
    overflow: hidden;
  }
  .card--front { left: 0; }
  .card--back { left: 635px; }
  .card__bands {
    position: absolute;
    left: 0; top: 0;
    width: 100%; height: 100%;
  }
  .brand-mark {
    position: absolute;
    left: 10px;
    top: 140px;
    width: 72px;
    text-align: center;
    font-family: "Tinos", serif;
    color: var(--wine);
    font-size: 12px;
    line-height: 15px;
  }
  .divider {
    position: absolute;
    left: 92px; top: 83px;
    width: 2px; height: 210px;
    background: var(--wine);
  }
  .person {
    position: absolute;
    left: 129px; width: 300px; top: 82px;
    text-align: center;
  }
  .person__name {
    font-family: "Tinos", serif;
    font-size: 21px; line-height: 24px;
    color: var(--ink);
  }
  .person__role {
    font-family: "Roboto", sans-serif; font-weight: 700;
    font-size: 13px; line-height: 18px;
    margin-top: 1px;
    color: var(--wine);
  }
  .person__email {
    font-family: "Roboto", sans-serif; font-weight: 700;
    font-size: 12.5px; line-height: 18px;
    color: var(--ink);
  }
  .contacts { position: absolute; left: 118px; top: 0; margin: 0; padding: 0; list-style: none; }
  .contacts__item {
    position: absolute; left: 0;
    display: flex; align-items: center;
    white-space: nowrap;
    font-family: "Roboto", sans-serif; font-weight: 700;
    font-size: 12.5px;
    color: var(--ink);
  }
  .contacts__icon { width: 28px; height: 28px; margin-right: 11px; flex: none; }
  .back-brand {
    position: absolute;
    left: 72px; top: 105px;
    display: flex; align-items: center;
    font-family: "Tinos", serif;
    color: var(--wine);
  }
  .back-brand__dot {
    width: 74px; height: 74px;
    border-radius: 50%;
    background: var(--wine);
    margin-right: 16px;
    flex: none;
  }
  .back-brand__name { display: block; font-size: 46px; line-height: 46px; letter-spacing: 1px; }
  .back-brand__sub { display: block; font-size: 18px; line-height: 24px; letter-spacing: 6px; text-align: right; }
</style>
</head>
<body>
<div class="sheet">

  <section class="card card--front">
    <svg class="card__bands" viewBox="0 0 1068 604" aria-hidden="true">
      <g>
        <circle cx="1200" cy="-138" r="462" fill="var(--ink)"/>
        <circle cx="1200" cy="-150" r="462" fill="var(--wine)"/>
        <circle cx="1200" cy="-150" r="369" fill="var(--paper)"/>
        <circle cx="1200" cy="-138" r="318" fill="var(--ink)"/>
        <circle cx="1200" cy="-150" r="318" fill="var(--wine)"/>
        <circle cx="1200" cy="-150" r="227" fill="var(--paper)"/>
      </g>
      <g>
        <circle cx="1200" cy="742" r="462" fill="var(--ink)"/>
        <circle cx="1200" cy="754" r="462" fill="var(--wine)"/>
        <circle cx="1200" cy="754" r="369" fill="var(--paper)"/>
        <circle cx="1200" cy="742" r="318" fill="var(--ink)"/>
        <circle cx="1200" cy="754" r="318" fill="var(--wine)"/>
        <circle cx="1200" cy="754" r="227" fill="var(--paper)"/>
      </g>
      <g>
        <circle cx="-102" cy="708" r="283" fill="var(--ink)"/>
        <circle cx="-90" cy="720" r="283" fill="var(--wine)"/>
      </g>
    </svg>

    <div class="brand-mark">Brambleford<br>Wine<br>Cellar</div>

    <div class="divider"></div>

    <div class="person">
      <div class="person__name">Mara Ellison</div>
      <div class="person__role">General Manager</div>
      <div class="person__email">bramblefordwinecellar@mailbox.example</div>
    </div>

    <ul class="contacts">
      <li class="contacts__item" style="top:158px">
        <svg class="contacts__icon" viewBox="0 0 28 28" aria-hidden="true">
          <circle cx="14" cy="14" r="12.5" fill="none" stroke="var(--wine)" stroke-width="2.5"/>
          <path d="M14 21 C10 16 9 13.5 9 11.5 a5 5 0 0 1 10 0 C19 13.5 18 16 14 21 Z" fill="var(--ink)"/>
          <circle cx="14" cy="11.5" r="2" fill="var(--paper)"/>
        </svg>
        42 Carrow Steet, Wexbury, Victoria, Australia 3207
      </li>
      <li class="contacts__item" style="top:191px">
        <svg class="contacts__icon" viewBox="0 0 28 28" aria-hidden="true">
          <circle cx="14" cy="14" r="12.5" fill="none" stroke="var(--wine)" stroke-width="2.5"/>
          <path d="M9 8 l3 -1 2 4 -2 1.5 c1 2 2 3 4 4 l1.5 -2 4 2 -1 3 c-6 1 -12 -5 -11.5 -11.5z" fill="var(--ink)"/>
          <path d="M16 8 a4 4 0 0 1 4 4 M16 5 a7 7 0 0 1 7 7" fill="none" stroke="var(--ink)" stroke-width="1.3"/>
        </svg>
        +61 3 9418 7360
      </li>
      <li class="contacts__item" style="top:223px">
        <svg class="contacts__icon" viewBox="0 0 28 28" aria-hidden="true">
          <circle cx="14" cy="14" r="12.5" fill="none" stroke="var(--wine)" stroke-width="2.5"/>
          <circle cx="14" cy="14" r="7.5" fill="var(--ink)"/>
          <g fill="none" stroke="var(--paper)" stroke-width="0.9">
            <ellipse cx="14" cy="14" rx="3.2" ry="7.5"/>
            <line x1="6.5" y1="14" x2="21.5" y2="14"/>
            <path d="M8 10 h12 M8 18 h12"/>
          </g>
        </svg>
        www.bramblefordwinecellar.example.au
      </li>
      <li class="contacts__item" style="top:258px">
        <svg class="contacts__icon" viewBox="0 0 28 28" aria-hidden="true">
          <circle cx="14" cy="14" r="12.5" fill="none" stroke="var(--wine)" stroke-width="2.5"/>
          <rect x="7" y="9.5" width="14" height="9.5" fill="var(--ink)"/>
          <path d="M7 9.5 l7 5.5 7 -5.5 M7 19 l5 -4.5 M21 19 l-5 -4.5" fill="none" stroke="var(--paper)" stroke-width="1"/>
        </svg>
        bramblefordwinecellar@mailbox.example
      </li>
    </ul>
  </section>

  <section class="card card--back">
    <svg class="card__bands" viewBox="0 0 1068 604" aria-hidden="true">
      <g>
        <circle cx="1200" cy="-138" r="462" fill="var(--ink)"/>
        <circle cx="1200" cy="-150" r="462" fill="var(--wine)"/>
        <circle cx="1200" cy="-150" r="369" fill="var(--paper)"/>
        <circle cx="1200" cy="-138" r="318" fill="var(--ink)"/>
        <circle cx="1200" cy="-150" r="318" fill="var(--wine)"/>
        <circle cx="1200" cy="-150" r="227" fill="var(--paper)"/>
      </g>
      <g>
        <circle cx="1200" cy="742" r="462" fill="var(--ink)"/>
        <circle cx="1200" cy="754" r="462" fill="var(--wine)"/>
        <circle cx="1200" cy="754" r="369" fill="var(--paper)"/>
        <circle cx="1200" cy="742" r="318" fill="var(--ink)"/>
        <circle cx="1200" cy="754" r="318" fill="var(--wine)"/>
        <circle cx="1200" cy="754" r="227" fill="var(--paper)"/>
      </g>
      <g>
        <circle cx="-102" cy="708" r="283" fill="var(--ink)"/>
        <circle cx="-90" cy="720" r="283" fill="var(--wine)"/>
      </g>
    </svg>

    <div class="back-brand">
      <span class="back-brand__dot"></span>
      <div>
        <span class="back-brand__name">Brambleford</span>
        <span class="back-brand__sub">Wine Cellar</span>
      </div>
    </div>
  </section>

</div>
</body>
</html>
```